BLENOX - Joining Study and Progress for Fair Opportunity

Brochure is needed for the European Project "BLENOX". We will distribute this flyer during conferences and events to our audiences (mainly academics, researchers, business individuals, policy makers and members of civil society groups) in order to provide the basic information about the project.
The main scope of the project is to support research organisations across Europe to design and implement gender equality plans in order to promote the women’s position of the filed of STEM research.

We are providing a video to explain the layout: https://www.vidstreamhub.example/watch?v=Xk4pR9tLm2Z.
We think size can range from A4-A3.

We are attaching files to provide with concrete information on our requirements:
- BLENOX Brochure Layout_SA.ppt: includes the content we would like to include in the flyer. There is also the URL to the project website
- blenox Logo.zip: the project logo
- Partners Logos.zip: the Logos that will be included
We would like to use colours that belong to the project logo colour range. Regarding the images that you may include in the flyer, we wouldn't like to propose any because we do not want to limitate your imagination. We have some at the website https://blenox-project.example/. They could be diverse (age, race, gender, etc.) relevant to women and men.

```html
<!DOCTYPE html>
<html lang="en">
<head>
<meta charset="utf-8">
<title>BLENOX – Joining Study and Progress for Fair Opportunity</title>
<link rel="stylesheet" href="https://fonts.googleapis.com/css2?family=Montserrat:wght@400;500;600;700;800&display=swap">
<style>
  :root{
    --purple:#4e3fa8;
    --purple-deep:#3d2f8f;
    --yellow:#f3b21c;
    --white:#ffffff;
    --ink:#3a3368;
    --muted:#5b5680;
    --badge:#ecebf3;
    --stage:#e6e5ec;
    --photo-a:#b9b4c9;
    --photo-b:#e7e2d9;
  }
  *{margin:0;padding:0;box-sizing:border-box}
  html,body{width:729px;height:1200px;overflow:hidden;background:var(--stage)}
  body{font-family:"Montserrat",Arial,sans-serif;color:var(--ink)}
  .page{position:absolute;overflow:hidden;background:var(--white)}
  .page svg.deco{position:absolute;left:0;top:0}
  .abs{position:absolute}

  /* ---------- inside spread ---------- */
  .inside-left{left:12px;top:12px;width:352px;height:500px}
  .inside-right{left:365px;top:12px;width:352px;height:500px}

  .sec-title{font-size:16px;font-weight:800;color:var(--purple);letter-spacing:.5px}
  .body-copy{font-size:7px;line-height:1.5;color:var(--muted)}
  .impact-title{left:196px;top:20px}
  .impact-copy{left:196px;top:44px;width:142px}
  .impact-list{left:196px;top:118px;width:142px;list-style:none}
  .impact-list li{display:flex;align-items:center;gap:6px;font-size:6.5px;line-height:1.3;color:var(--ink);margin-bottom:7px}
  .impact-icon{flex:none;width:14px;height:14px;border-radius:50%;background:var(--purple)}

  .goal-title{left:20px;top:212px;display:flex;align-items:baseline;gap:5px}
  .goal-the{font-size:10px;font-weight:800;color:var(--yellow)}
  .goal-main{font-size:18px;font-weight:800;color:var(--purple)}
  .goal-copy{left:20px;top:240px;width:312px}

  .hubs-title{left:20px;top:322px;font-size:10px;font-weight:700;color:var(--yellow)}
  .hubs-list{left:20px;top:342px;width:180px;list-style:none}
  .hubs-list li{display:flex;align-items:center;gap:6px;font-size:7px;color:var(--white);margin-bottom:8px}
  .hub-dot{flex:none;width:7px;height:7px;border-radius:50%;background:var(--yellow)}

  .consortium-title{left:20px;top:20px}
  .consortium-copy{left:20px;top:44px;width:312px}
  .badges{left:20px;top:112px;width:312px;display:grid;grid-template-columns:repeat(4,1fr);gap:10px 12px}
  .badge{height:26px;border-radius:4px;background:var(--badge)}
  .back-title{left:20px;top:408px;width:170px;font-size:10px;line-height:1.35;font-weight:800;text-transform:uppercase;color:var(--yellow)}
  .back-brand{left:20px;top:458px;display:flex;align-items:center;gap:8px}
  .back-dot{width:18px;height:18px;border-radius:50%;background:var(--yellow)}
  .back-name{font-size:17px;font-weight:700;letter-spacing:2px;color:var(--white)}

  /* ---------- front cover ---------- */
  .cover{left:130px;top:524px;width:470px;height:664px}
  .brand{left:0;top:28px;width:100%;display:flex;justify-content:center;align-items:center;gap:10px}
  .brand-dot{width:26px;height:26px;border-radius:50%;background:var(--yellow)}
  .brand-name{font-size:28px;font-weight:700;letter-spacing:3px;color:var(--purple)}
  .title{left:35px;top:84px;width:400px;text-align:center;font-size:18px;line-height:1.25;font-weight:800;text-transform:uppercase;color:var(--purple)}
  .band{left:0;top:170px;width:470px;height:430px;background:var(--purple)}
  .join{left:0;top:186px;width:100%;text-align:center;font-size:22px;font-weight:800;color:var(--yellow)}
  .join-text{left:55px;top:220px;width:360px;text-align:center;font-size:9px;line-height:1.5;color:var(--white)}
  .link-pill{left:50%;top:272px;transform:translateX(-50%);padding:5px 16px;border-radius:14px;background:var(--white);color:var(--purple);font-size:9px;font-weight:600;white-space:nowrap}
  .visual{left:0;top:305px}
  .footer-text{left:20px;top:610px;width:430px;text-align:center;font-size:8px;color:var(--ink)}
  .socials{left:0;top:632px;width:100%;display:flex;justify-content:center;gap:30px}
  .social{display:flex;align-items:center;gap:6px;font-size:8px;font-weight:600;color:var(--purple)}
  .social-dot{width:18px;height:18px;border-radius:50%;background:var(--purple)}
</style>
</head>
<body>

<!-- Inside left page: goal and impact -->
<section class="page inside-left">
  <svg class="deco" width="352" height="500" viewBox="0 0 352 500" xmlns="http://www.w3.org/2000/svg">
    <defs>
      <linearGradient id="toneA" x1="0" y1="0" x2="1" y2="1">
        <stop offset="0" stop-color="#e7e2d9"/><stop offset="1" stop-color="#b9b4c9"/>
      </linearGradient>
    </defs>
    <path d="M0 310 Q120 280 352 300 L352 500 L0 500 Z" fill="var(--purple)"/>
    <path d="M20 150 A100 100 0 0 1 170 40" fill="none" stroke="var(--yellow)" stroke-width="14" stroke-linecap="round"/>
    <g role="img" aria-label="Photo of researchers discussing around a laptop">
      <path d="M105 22 A80 80 0 1 1 70 170 L45 195 L58 160 A80 80 0 0 1 105 22 Z" fill="url(#toneA)" stroke="var(--white)" stroke-width="4"/>
    </g>
    <path d="M340 360 A75 75 0 0 1 230 480" fill="none" stroke="var(--yellow)" stroke-width="10" stroke-linecap="round"/>
    <g role="img" aria-label="Photo of a woman and a man working together at a desk">
      <circle cx="272" cy="425" r="62" fill="url(#toneA)" stroke="var(--white)" stroke-width="4"/>
    </g>
  </svg>

  <h2 class="abs sec-title impact-title">IMPACT</h2>
  <p class="abs body-copy impact-copy">BLENOX helps research bodies turn gender equality plans into daily practice, building fairer careers and stronger teams in science and innovation across Europe.</p>
  <ul class="abs impact-list">
    <li><span class="impact-icon"></span>Fair plans in place at partner bodies</li>
    <li><span class="impact-icon"></span>Shared tools for leaders and staff</li>
    <li><span class="impact-icon"></span>Wider networks for women in STEM</li>
    <li><span class="impact-icon"></span>Lasting change in research policy</li>
  </ul>

  <h2 class="abs goal-title"><span class="goal-the">THE</span><span class="goal-main">GOAL</span></h2>
  <p class="abs body-copy goal-copy">The main aim of BLENOX is to support research organisations across Europe to design and apply gender equality plans that raise the position of women in STEM research, through local hubs, training and shared learning.</p>

  <h3 class="abs hubs-title">BLENOX Research &amp; Innovation Hubs</h3>
  <ul class="abs hubs-list">
    <li><span class="hub-dot"></span>Hub one: Life sciences</li>
    <li><span class="hub-dot"></span>Hub two: Engineering</li>
    <li><span class="hub-dot"></span>Hub three: Digital tech</li>
    <li><span class="hub-dot"></span>Hub four: Energy and climate</li>
    <li><span class="hub-dot"></span>Hub five: Social science</li>
  </ul>
</section>

<!-- Inside right page: consortium -->
<section class="page inside-right">
  <svg class="deco" width="352" height="500" viewBox="0 0 352 500" xmlns="http://www.w3.org/2000/svg">
    <defs>
      <linearGradient id="toneB" x1="0" y1="0" x2="1" y2="1">
        <stop offset="0" stop-color="#e7e2d9"/><stop offset="1" stop-color="#b9b4c9"/>
      </linearGradient>
    </defs>
    <path d="M0 330 Q150 290 352 360 L352 500 L0 500 Z" fill="var(--purple)"/>
    <path d="M150 260 A95 95 0 0 1 320 230" fill="none" stroke="var(--yellow)" stroke-width="12" stroke-linecap="round"/>
    <g role="img" aria-label="Photo of two colleagues reviewing documents together">
      <path d="M255 225 A78 78 0 1 1 200 360 L180 385 L188 350 A78 78 0 0 1 255 225 Z" fill="url(#toneB)" stroke="var(--white)" stroke-width="4"/>
    </g>
  </svg>

  <h2 class="abs sec-title consortium-title">CONSORTIUM</h2>
  <p class="abs body-copy consortium-copy">The BLENOX consortium brings together universities, research centres, business networks and civil society groups from across Europe, each sharing skills to build and test fair plans in real settings.</p>
  <div class="abs badges" aria-label="Partner badges">
    <span class="badge"></span><span class="badge"></span><span class="badge"></span><span class="badge"></span>
    <span class="badge"></span><span class="badge"></span><span class="badge"></span><span class="badge"></span>
    <span class="badge"></span><span class="badge"></span><span class="badge"></span><span class="badge"></span>
  </div>

  <p class="abs back-title">Joining Study and Progress for Fair Opportunity</p>
  <div class="abs back-brand"><span class="back-dot"></span><span class="back-name">BLENOX</span></div>
</section>

<!-- Front cover -->
<section class="page cover">
  <header class="abs brand">
    <span class="brand-dot"></span>
    <span class="brand-name">BLENOX</span>
  </header>
  <h1 class="abs title">Joining Study and Progress<br>for Fair Opportunity</h1>

  <div class="abs band"></div>
  <h2 class="abs join">JOIN BLENOX</h2>
  <p class="abs join-text">Our project supports research bodies across Europe to build and apply gender equality plans that strengthen the position of women in STEM research and innovation.</p>
  <div class="abs link-pill">https://blenox-project.example/</div>

  <svg class="abs visual" width="470" height="295" viewBox="0 0 470 295" xmlns="http://www.w3.org/2000/svg">
    <defs>
      <linearGradient id="toneC" x1="0" y1="0" x2="1" y2="1">
        <stop offset="0" stop-color="#e7e2d9"/><stop offset="1" stop-color="#b9b4c9"/>
      </linearGradient>
    </defs>
    <path d="M85 170 A140 140 0 0 1 350 70" fill="none" stroke="var(--yellow)" stroke-width="18" stroke-linecap="round"/>
    <path d="M395 190 A140 140 0 0 1 160 285" fill="none" stroke="var(--yellow)" stroke-width="12" stroke-linecap="round"/>
    <g role="img" aria-label="Photo of a diverse team of researchers working together around a laptop">
      <path d="M235 40 A115 115 0 1 1 150 235 L120 280 L136 222 A115 115 0 0 1 235 40 Z" fill="url(#toneC)" stroke="var(--white)" stroke-width="5"/>
    </g>
  </svg>

  <p class="abs footer-text">Follow BLENOX and subscribe to our newsletter for the latest updates on our activities.</p>
  <div class="abs socials">
    <span class="social"><span class="social-dot"></span>@blenoxproject</span>
    <span class="social"><span class="social-dot"></span>@blenoxproject</span>
    <span class="social"><span class="social-dot"></span>@blenoxproject</span>
  </div>
</section>

</body>
</html>
```